Homeowners Insurance Provider Website

We are selling homeowners insurance policy / tenants Policy/Flood Insurance in USA in few states and planning expand nationally.

Our target audience are two folds: Customers (Buy policies) and Insurance Agents who wants to work with us to sell our policies to customers. But website should focus 80% on customers and 20% on agents. So, more customer focused user experience. Please note that there is no direct buy option for customers. They always go through insurance agents.

Customer focused, educational that makes buyer journey easy. We don’t want to come off as trying sell something as there is no direct sales involved from website.

Target Market(s)

Homeowners in USA and Insurance agent who sells these insurance.

Industry/Entity Type

Insurance

Number of Pages Required

4 page

Font styles to use
Other font styles liked:
• Open to suggestions

Colors

Designer to choose colors to be used in the design.

Requirements
Must have
• Three most important things: Trustworthy, Authentic, Simple
• Please use colors form logo and grays
• We like: www.harborlane.com
• https://www.veltrimoor.com/
• We need Agent Look up tool on home page similar to what is shown on example sites.
• Design:
• Home Page - Open to Ideas
• Insurance (Products) Landing Page - Info similar to: https://www.veltrimoor.com/insurance/
• Agents Page - https://www.veltrimoor.com/agents/
• Claims Page - Information similar to: https://www.veltrimoor.com/claims-center/
• Site Navigation:
• Home
• Insurance
• Claims
• Agents
• About Us
• Contact Us
Nice to have
• Elegant, minimal and clean design that reflects trust and authenticity.
Should not have
• Slider or rotating images - prefer flat design. Not over powering design.

```html
<!DOCTYPE html>
<html lang="en">
<head>
<meta charset="utf-8">
<title>Hearthstead Insurance Co.</title>
<link href="https://fonts.googleapis.com/css2?family=Open+Sans:wght@400;600;700&family=Raleway:wght@400;500;600&display=swap" rel="stylesheet">
<style>
:root{
  --red:#d0202e;
  --navy:#1f3b7c;
  --navy-deep:#14285a;
  --ink:#2a2a2a;
  --gray:#5a5a5a;
  --line:#c9c9c9;
  --light:#f3f3f3;
  --footer:#1c1c1c;
  --white:#ffffff;
}
*{box-sizing:border-box;margin:0;padding:0}
html,body{width:1200px;height:2903px;overflow:hidden}
body{position:relative;font-family:"Raleway",sans-serif;color:var(--ink);background:var(--white)}
.abs{position:absolute}
h2,h3,.heading{font-family:"Open Sans",sans-serif}
.btn{display:inline-block;font-family:"Open Sans",sans-serif;font-size:12px;font-weight:600;text-transform:uppercase;color:var(--white);text-align:center;letter-spacing:.3px}
.btn-red{background:var(--red)}
.btn-navy{background:var(--navy)}
.btn-ghost{border:1px solid #fff}
.lorem{font-size:13px;line-height:23px;color:var(--gray)}

/* header */
.site-header{left:0;top:0;width:1200px;height:86px;background:rgba(235,235,238,.93);z-index:3}
.brand{left:150px;top:14px;display:flex;align-items:center;gap:12px}
.brand-mark{width:50px;height:56px;background:var(--navy)}
.brand-name{font-family:"Open Sans",sans-serif;font-weight:700;font-size:22px;line-height:25px;color:var(--navy)}
.main-nav{right:140px;top:30px;display:flex;align-items:center;gap:19px;font-family:"Open Sans",sans-serif;font-size:13px;color:#333}
.main-nav .active{color:var(--red)}
.main-nav .quote{background:var(--navy);color:#fff;padding:6px 9px}

/* hero */
.hero{left:0;top:0;width:1200px;height:548px;background:linear-gradient(100deg,#273554 0%,#3a4a6c 45%,#8e96aa 72%,#2c3754 100%)}
.hero-box{left:141px;top:269px;width:492px;height:143px;background:rgba(235,235,238,.92);border-radius:8px;padding:18px 18px}
.hero-box h1{font-family:"Open Sans",sans-serif;font-weight:600;font-size:25px;line-height:33px;color:#222;letter-spacing:.5px}
.hero-more{left:164px;top:397px;width:105px;height:30px;line-height:30px}

.feature{width:190px;text-align:center}
.feature-ring{width:174px;height:174px;margin:0 auto;border-radius:50%;background:var(--white);border:10px solid #e3e3e6;box-shadow:0 -4px 0 #c6c8cf;display:flex;align-items:center;justify-content:center}
.feature-label{margin-top:14px;font-family:"Open Sans",sans-serif;font-size:16px;line-height:21px;font-weight:600;color:var(--red);text-transform:uppercase}

/* about */
.section-title{font-family:"Open Sans",sans-serif;font-size:26px;font-weight:600;color:#222;letter-spacing:.5px}
.rule{height:2px;background:var(--line)}
.rule::before{content:"";display:block;width:62px;height:4px;margin-top:-1px;background:var(--navy)}
.quote-card{left:818px;top:720px;width:240px;height:282px;background:#ececec;border:1px solid #ddd}
.quote-card h3{height:36px;line-height:36px;text-align:center;background:var(--navy);color:#fff;font-size:20px;font-weight:600}
.field{height:31px;margin:0 14px 9px;background:#f7f7f7;border:1px solid #d6d6d6;font-size:10px;color:#777;padding:0 10px;line-height:31px}
.field-tall{height:50px}

/* audience panels */
.panel{top:1060px;width:600px;height:325px;color:#fff;text-align:center}
.panel-customers{left:0;background:linear-gradient(90deg,#2a2a2a,#4a4a4a 60%,#2b2b2b)}
.panel-agents{left:600px;background:linear-gradient(90deg,#b8121d,#d8222d 60%,#9c0f18)}
.panel h3{font-size:20px;font-weight:600;margin-top:10px}
.panel p{font-size:13px;line-height:23px;width:380px;margin:8px auto 0}
.panel .btn{margin-top:14px;width:128px;height:29px;line-height:27px}

/* insurance */
.insurance{left:0;top:1385px;width:1200px;height:627px;background:var(--light)}
.ins-card{top:1542px;width:306px;height:414px;color:#fff;text-align:center}
.ins-card .inner{position:absolute;left:0;right:0;bottom:0;padding:0 22px 26px}
.ins-card h3{font-size:19px;font-weight:600}
.ins-card h3::after{content:"";display:block;width:62px;height:3px;background:var(--red);margin:8px auto 14px}
.ins-card p{font-size:11px;line-height:19px;color:#eee}
.ins-actions{display:flex;justify-content:center;gap:14px;margin-top:12px}
.ins-actions .btn{height:30px;line-height:30px;font-size:11px}

/* find agent */
.find-agent{left:0;top:2012px;width:1200px;height:293px;background:var(--navy-deep);color:#fff;text-align:center}
.find-agent h2{font-size:25px;font-weight:600;margin-top:62px;letter-spacing:.5px}
.find-agent .bar{width:62px;height:3px;background:#fff;margin:8px auto 18px}
.find-agent p{width:620px;margin:0 auto;font-size:13px;line-height:23px;color:#dfe4f0}
.search-row{display:flex;justify-content:center;gap:8px;margin-top:20px}
.search-row .input{width:156px;height:30px;background:#fff;color:#777;font-size:11px;line-height:30px;padding-left:8px;text-align:left}
.search-row .btn{width:156px;height:30px;line-height:30px}

/* claim + contact */
.claim{left:160px;top:2360px;width:270px;text-align:center}
.claim .kicker{font-family:"Open Sans",sans-serif;font-size:24px;font-weight:600;color:var(--navy-deep)}
.claim .big{font-family:"Open Sans",sans-serif;font-size:50px;font-weight:700;color:var(--red);line-height:60px}
.claim p{font-size:14px;line-height:22px;color:var(--navy)}
.claim .btn{margin-top:28px;width:86px;height:30px;line-height:30px}
.divider-v{left:455px;top:2360px;width:1px;height:210px;background:var(--line)}
.contact{left:485px;top:2352px;width:526px}
.contact .small{font-size:11px;color:#444;margin:26px 0 8px}
.contact .grid{display:grid;grid-template-columns:258px 258px;gap:13px 12px}
.contact .field{margin:0;background:#fff}
.contact .btn{margin-top:15px;width:86px;height:28px;line-height:28px}

/* footer */
.site-footer{left:0;top:2618px;width:1200px;height:248px;background:var(--footer);color:#ddd}
.foot-col{top:38px}
.foot-col h4{font-family:"Open Sans",sans-serif;font-size:16px;font-weight:400;color:#fff;padding-bottom:12px;border-bottom:1px solid #3a3a3a;margin-bottom:16px}
.quick li{list-style:none;font-size:11px;line-height:22px;color:#ccc}
.quick li::before{content:"› ";color:#888}
.quick li.active{color:var(--navy)}
.foot-text{font-size:11px;line-height:18px;color:#bbb}
.foot-contact{display:flex;align-items:center;gap:10px;font-size:15px;color:#ddd;margin-top:22px}
.news-input{width:172px;height:28px;background:#4a4a4a;color:#ddd;font-size:11px;line-height:28px;padding-left:10px;margin-top:14px}
.news .btn{margin-top:10px;width:92px;height:26px;line-height:26px;text-transform:none;font-size:12px}
.foot-name{left:880px;top:95px;font-family:"Open Sans",sans-serif;font-size:20px;font-weight:600;color:#9a9a9a;display:flex;align-items:center;gap:10px}
.foot-name span.sq{width:22px;height:22px;background:#9a9a9a}
.bottom-bar{left:0;top:2866px;width:1200px;height:37px;background:var(--navy);color:#fff;font-size:11px;font-weight:600}
.socials{right:142px;top:10px;display:flex;gap:6px}
.socials span{width:18px;height:18px;background:#fff;opacity:.85}
</style>
</head>
<body>

<header class="abs site-header">
  <div class="abs brand">
    <span class="brand-mark"></span>
    <span class="brand-name">HEARTHSTEAD<br>INSURANCE CO.</span>
  </div>
  <nav class="abs main-nav">
    <span class="active">Home</span><span>About Us</span><span>Insurance</span><span>Agents</span><span>Claims</span><span>Contact Us</span><span class="quote">Get a quote</span>
  </nav>
</header>

<section class="abs hero" role="img" aria-label="Photo of a businessman's hands sheltering a small model house"></section>
<div class="abs hero-box"><h1>GET HOMEOWNERS INSURANCE POLICY / TENANTS POLICY/ FLOOD INSURANCE IN USA</h1></div>
<span class="abs btn btn-red hero-more">Read more</span>

<div class="abs feature" style="left:215px;top:460px">
  <div class="feature-ring">
    <svg width="56" height="56" viewBox="0 0 56 56" fill="#d0202e"><path d="M28 6 6 26h7v16h30V26h7z"/><text x="28" y="38" font-size="16" font-family="Open Sans" font-weight="700" fill="#fff" text-anchor="middle">%</text><rect x="4" y="44" width="48" height="6" rx="3"/></svg>
  </div>
  <div class="feature-label">Homeowners<br>Policy</div>
</div>
<div class="abs feature" style="left:499px;top:460px">
  <div class="feature-ring">
    <svg width="56" height="56" viewBox="0 0 56 56" fill="#d0202e"><path d="M28 4 4 24h6v26h36V24h6z"/><circle cx="22" cy="28" r="4" fill="#fff"/><circle cx="34" cy="28" r="4" fill="#fff"/><rect x="18" y="33" width="8" height="14" fill="#fff"/><rect x="30" y="33" width="8" height="14" fill="#fff"/></svg>
  </div>
  <div class="feature-label">Tenants Policy</div>
</div>
<div class="abs feature" style="left:785px;top:460px">
  <div class="feature-ring">
    <svg width="56" height="56" viewBox="0 0 56 56" fill="none" stroke="#d0202e" stroke-width="3"><path d="M28 8 10 24v12h36V24z" fill="#d0202e"/><path d="M6 42q5-4 10 0t11 0 11 0 11 0M6 50q5-4 10 0t11 0 11 0 11 0"/></svg>
  </div>
  <div class="feature-label">Flood Insurance</div>
</div>

<!-- about -->
<h2 class="abs section-title" style="left:141px;top:732px">ABOUT US</h2>
<div class="abs rule" style="left:141px;top:788px;width:617px"></div>
<p class="abs lorem" style="left:145px;top:807px;width:612px">Lorem ipsum dolor sit amet, consectetuer adipiscing elit, sed diam nonummy nibh euismod tincidunt ut laoreet dolore magna aliquam erat volutpat. Ut wisi enim ad minim veniam, quis nostrud exerci tation ullamcorper suscipit lobortis nisl ut aliquip ex ea commodo consequat. Duis autem vel eum iriure dolor in hendrerit in vulputate velit esse molestie consequat, vel illum dolore eu feugiat nulla facilisis at vero eros et accumsan et iusto odio dignissim qui blandit praesent luptatum zzril delenit augue duis dolore te feugait nulla facilisi.</p>
<span class="abs btn btn-navy" style="left:141px;top:971px;width:130px;height:29px;line-height:29px">Read more</span>

<form class="abs quote-card">
  <h3>Get A Quote</h3>
  <div style="height:16px"></div>
  <div class="field">Name</div>
  <div class="field">Email</div>
  <div class="field">Subject</div>
  <div class="field field-tall">Message</div>
  <span class="btn btn-navy" style="display:block;margin:0 14px;height:31px;line-height:31px">Submit</span>
</form>

<!-- audience -->
<section class="abs panel panel-customers" role="img" aria-label="Photo of customers shaking hands with an advisor">
  <svg style="margin-top:44px" width="70" height="44" viewBox="0 0 70 44" fill="#fff"><path d="M4 10h14l12 6 10-6h12l14 6v16l-10 6-6-4-8 6-20-8-18-4z"/></svg>
  <h3>Customers</h3>
  <p>Lorem ipsum dolor sit amet, consectetuer adipiscing elit, sed diam nonummy nibh euismod tincidunt ut laoreet dolore magna aliquam erat volutpat</p>
  <span class="btn btn-ghost">Read more</span>
</section>
<section class="abs panel panel-agents" role="img" aria-label="Photo of an insurance agent working at a laptop, red tinted">
  <svg style="margin-top:36px" width="70" height="70" viewBox="0 0 70 70"><circle cx="35" cy="35" r="33" fill="#fff"/><circle cx="35" cy="24" r="7" fill="#d0202e"/><path d="M24 48q0-14 11-14t11 14z" fill="#d0202e"/><circle cx="19" cy="30" r="5" fill="#d0202e"/><circle cx="51" cy="30" r="5" fill="#d0202e"/></svg>
  <h3>Agents</h3>
  <p>Lorem ipsum dolor sit amet, consectetuer adipiscing elit, sed diam nonummy nibh euismod tincidunt ut laoreet dolore magna aliquam erat volutpat</p>
  <span class="btn btn-ghost">Read more</span>
</section>

<!-- insurance -->
<section class="abs insurance"></section>
<h2 class="abs section-title" style="left:0;width:1200px;text-align:center;top:1432px">INSURANCE</h2>
<div class="abs rule" style="left:292px;top:1490px;width:616px"></div>
<div class="abs" style="left:569px;top:1488px;width:62px;height:4px;background:var(--navy)"></div>

<article class="abs ins-card" style="left:141px;background:linear-gradient(180deg,#dcdcdc 0%,#8f8f8f 45%,#1a1a1a 100%)" role="img" aria-label="Photo of a couple in their new home">
  <div class="inner">
    <h3>Homeowner Policy</h3>
    <p>Lorem ipsum dolor sit amet, consectetuer adipiscing elit, sed diam nonummy nibh euismod tincidunt ut laoreet dolore magna aliquam erat volutpat.</p>
    <div class="ins-actions"><span class="btn btn-red" style="width:108px">Quote →</span><span class="btn btn-navy" style="width:132px">Read more →</span></div>
  </div>
</article>
<article class="abs ins-card" style="left:447px;background:linear-gradient(180deg,#d9c4a8 0%,#b88f6a 40%,#2f4a8a 52%,#2f4a8a 100%)" role="img" aria-label="Photo of smiling tenants reading together">
  <div class="inner" style="padding-bottom:38px">
    <h3>Tenant Policy</h3>
    <p>Lorem ipsum dolor sit amet, consectetuer adipiscing elit, sed diam nonummy nibh euismod tincidunt ut laoreet dolore magna aliquam erat volutpat.</p>
    <div class="ins-actions"><span class="btn btn-red" style="width:108px">Quote →</span><span class="btn" style="width:132px;background:#fff;color:var(--red)">Read more →</span></div>
  </div>
</article>
<article class="abs ins-card" style="left:753px;background:linear-gradient(180deg,#5f8a48 0%,#7a3a30 45%,#1a1a1a 100%)" role="img" aria-label="Photo of a house damaged by flooding">
  <div class="inner">
    <h3>Flood Policy</h3>
    <p>Lorem ipsum dolor sit amet, consectetuer adipiscing elit, sed diam nonummy nibh euismod tincidunt ut laoreet dolore magna aliquam erat volutpat.</p>
    <div class="ins-actions"><span class="btn btn-red" style="width:108px">Quote →</span><span class="btn btn-navy" style="width:132px">Read more →</span></div>
  </div>
</article>

<!-- find an agent -->
<section class="abs find-agent">
  <h2>FIND AN AGENT</h2>
  <div class="bar"></div>
  <p>Lorem ipsum dolor sit amet, consectetuer adipiscing elit, sed diam nonummy nibh euismod tincidunt ut laoreet dolore magna aliquam erat volutpat. Ut wisi enim ad minim veniam, quis nostrud exerci tation ullamcorper suscipit lobortis nisl ut aliquip ex ea commodo consequat.</p>
  <div class="search-row"><span class="input">Search...</span><span class="btn btn-red">Find an agent</span></div>
</section>

<!-- claim + contact -->
<div class="abs claim">
  <div class="kicker">Report And Check</div>
  <div class="big">A Claim</div>
  <p>Login To Report A Claim Or<br>Check Your Claim Status.</p>
  <span class="btn btn-red">Login</span>
</div>
<div class="abs divider-v"></div>
<form class="abs contact">
  <h2 class="section-title" style="font-size:25px">CONTACT FORM</h2>
  <div class="rule" style="margin-top:12px;width:530px"></div>
  <p class="small">Please fill up bellow form</p>
  <div class="grid">
    <div class="field">Name</div><div class="field">Email</div>
    <div class="field">Phone</div><div class="field">Message</div>
  </div>
  <span class="btn btn-red">Submit</span>
</form>

<!-- footer -->
<footer class="abs site-footer">
  <div class="abs foot-col" style="left:158px;width:130px">
    <h4>Quick Links</h4>
    <ul class="quick"><li class="active">Home</li><li>About Us</li><li>Insurance</li><li>Agents</li><li>Claims</li><li>Contact Us</li></ul>
  </div>
  <div class="abs foot-col" style="left:338px;width:190px">
    <h4>Contact Detail</h4>
    <p class="foot-text" style="color:#fff">Hearthstead Insurance</p>
    <p class="foot-text">Lorem ipsum dolor sit amet, consectetur adipiscing elit, sed do eiusmod</p>
    <div class="foot-contact"><svg width="14" height="14" viewBox="0 0 24 24" fill="#3f6fd0"><path d="M6 2l4 4-2 3q3 5 7 7l3-2 4 4-3 4Q8 20 2 5z"/></svg>123.456.7890</div>
    <div class="foot-contact" style="font-size:11px;margin-top:12px"><svg width="14" height="11" viewBox="0 0 14 11" fill="#3f6fd0"><rect width="14" height="11"/><path d="M0 0l7 6 7-6" stroke="#1c1c1c" fill="none"/></svg>info@hearthstead.com</div>
  </div>
  <div class="abs foot-col news" style="left:622px;width:214px">
    <h4>Join Our Newsletter</h4>
    <p class="foot-text">Subscribe to our Newsletter to get the latest scoop right to your inbox</p>
    <div class="news-input">Enter Your Email</div>
    <span class="btn btn-red">Subscribe</span>
  </div>
  <div class="abs foot-name"><span class="sq"></span>Hearthstead</div>
</footer>
<div class="abs bottom-bar">
  <span class="abs" style="left:142px;top:12px">© 2018 Hearthsteadinsurance. All Rights Reserved.</span>
  <div class="abs socials"><span></span><span></span><span></span></div>
</div>

</body>
</html>
```